Create a wordpress website for Dulvane business solution

This project is to create a complete website with all pages.

Overview
The purpose of this project is to create a full complete website with all pages (16 pages). The site should be professional and modern. The site is for an IT recruiting and IT training company. The site needs to be easy to administer and update content. It should be simple to add pages, videos and testimonials later. I will leave the site layout, color schemes and flow to the designers.

Navigation Menu (Home, who we are, what we do, what makes us different, why it matters, candidate portal, contact us, Blog)

WHO WE ARE should be a drop down menu with link to pages (about us, mission, vision and purpose, our team)

WHAT WE DO should be drop down menu with link to the following pages (IT Recruiting, IT Training, Hardware and software sales)

What makes us different should be single page with different paragraph titles. (We live what we do, we don't compromise quality, we share knowledge, staffing guarantee)

Why it matters should be single page with paragraph titles. (Quickly fill positions, candidate career development)

Candidate portal should links to my portal login page. I can add the correct URL later. I just need it to link to somewhere. I can change it.

Contact us should have (address, phone number, google map and a form to submit request for a call back)

Blog - This link should launch a wordpress blogging module

Target Market(s)

IT RECRUITING AND CONSULTING

Industry/Entity Type

It Company

Coding

Coded - Design and coding required

Requirements
Must have
• Company Logo
• Navigation Menu (Home, who we are, what we do, what makes us different, why it matters, candidate portal, contact us)
• WHO WE ARE should be a drop down menu with link to pages (about us, mission, vision and purpose, our team)
• WHAT WE DO should be drop down menu with link to the following pages (IT Recruiting, IT Training, Hardware and software sales)
• What makes us different should be single page with different paragraph titles. (We live what we do, we don't compromise quality, we share knowledge, staffing guarantee)
• Why it matters should be single page with paragraph titles. (Quickly fill positions, candidate career development)
• Candidate portal should links to my portal login page. I can add the correct URL later. I just need it to link to somewhere. I can change it.
• Contact us should have (address, phone number, google map and a form to submit request for a call back)

```html
<!DOCTYPE html>
<html lang="en">
<head>
<meta charset="utf-8">
<title>Dulvane Business Solution</title>
<link href="https://fonts.googleapis.com/css2?family=Lato:wght@300;400;700&display=swap" rel="stylesheet">
<style>
:root{
  --blue:#1b5fa0;
  --blue-dark:#0f4c8a;
  --orange:#e8731b;
  --orange-dark:#b8591a;
  --ink:#333;
  --muted:#666;
  --faint:#999;
  --line:#e2e2e2;
  --soft:#f8f8f8;
  --white:#fff;
}
*{margin:0;padding:0;box-sizing:border-box}
html,body{width:1200px;height:3607px;overflow:hidden}
body{font-family:"Lato",Arial,sans-serif;color:var(--ink);background:var(--white);position:relative}

/* header */
.site-header{position:absolute;top:0;left:0;width:1200px;height:72px;background:var(--white)}
.brand{position:absolute;left:212px;top:14px;display:flex;align-items:center;gap:8px}
.brand-mark{width:14px;height:14px;background:var(--blue)}
.brand-name{font-size:34px;font-weight:700;color:var(--blue);letter-spacing:0.5px;line-height:1}
.main-nav{position:absolute;left:392px;top:30px;display:flex;align-items:center;font-size:11.5px;color:#444}
.main-nav a{color:#444;text-decoration:none;padding:0 8px;line-height:24px;position:relative;white-space:nowrap}
.main-nav a.active:after{content:"";position:absolute;left:8px;right:8px;bottom:-6px;height:2px;background:var(--blue)}
.main-nav a.portal{background:var(--orange);color:var(--white);margin:0 6px;padding:0 10px}
.dropdown{position:absolute;left:423px;top:87px;width:135px;height:139px;background:rgba(15,76,138,0.92);padding:10px 18px;z-index:3}
.dropdown a{display:block;color:var(--white);font-size:10.5px;text-decoration:none;line-height:27px}

/* hero */
.hero{position:absolute;top:72px;left:0;width:1200px;height:553px;background:linear-gradient(100deg,#3a3f45 0%,#5b6068 35%,#6c747c 60%,#8b98a4 100%)}
.hero-shade{position:absolute;inset:0;background:rgba(20,28,38,0.35)}
.hero-title{position:absolute;top:298px;width:100%;text-align:center;color:var(--white);font-size:38px;font-weight:300;letter-spacing:0.3px}
.hero-arrow{position:absolute;top:275px}

/* section headings */
.section-title{position:absolute;left:0;width:1200px;text-align:center;font-size:27px;font-weight:400;color:#333;letter-spacing:0.5px}
.dots{position:absolute;left:583px;width:34px;display:flex;gap:5px}
.dots span{width:8px;height:8px;background:var(--orange)}
.dots span:nth-child(2){background:var(--orange-dark)}

/* services */
.service{position:absolute;top:818px;width:240px}
.service-head{display:flex;align-items:center;gap:14px;height:50px}
.service-head h3{font-size:14px;font-weight:400;color:#333}
.service p{margin-top:24px;font-size:11px;line-height:16px;color:var(--muted)}
.btn-sm{display:inline-block;margin-top:26px;background:var(--blue-dark);color:var(--white);font-size:9px;padding:0 12px;line-height:20px;text-decoration:none}

/* about */
.about{position:absolute;top:1087px;left:0;width:1200px;height:428px;background:var(--soft)}
.about-text{position:absolute;top:188px;left:200px;width:800px;text-align:center;font-size:13px;line-height:21px;color:#555}
.btn-orange{position:absolute;background:var(--orange);color:var(--white);font-size:10px;font-weight:700;text-align:center;text-decoration:none;letter-spacing:0.4px}

/* team */
.member{position:absolute;width:380px}
.member-photo{position:absolute;left:0;top:0;width:136px;height:120px;background:linear-gradient(160deg,#d9d4cf,#a39b94)}
.member-role{position:absolute;left:154px;top:30px;font-size:12.5px;color:#444}
.member-name{position:absolute;left:154px;top:48px;font-size:22px;color:var(--orange);font-weight:400;white-space:nowrap}
.member-org{position:absolute;left:154px;top:82px;font-size:10px;color:var(--faint)}
.member-bio{position:absolute;left:0;top:140px;width:380px;font-size:12.5px;line-height:20px;color:#555}

/* contact */
.contact{position:absolute;top:2304px;left:0;width:1200px;height:907px;background:var(--soft)}
.map{position:absolute;left:269px;top:149px;width:662px;height:277px;background:linear-gradient(135deg,#e8e1cf 0%,#dbe7c9 45%,#e9dfcc 70%,#d6e3c3 100%)}
.col-title{position:absolute;font-size:17px;color:var(--orange);letter-spacing:0.8px;font-weight:400}
.field{position:absolute;left:269px;width:320px;height:44px;border:1px solid var(--line);background:var(--white);font-size:12px;color:var(--faint);padding:14px 12px}
.address{position:absolute;left:628px;top:2833px;font-size:13px;line-height:23px;color:#777}

/* footer */
.site-footer{position:absolute;top:3211px;left:0;width:1200px;height:324px;background:var(--white)}
.foot-col{position:absolute;top:3262px}
.foot-col h4{font-size:13px;font-weight:400;color:var(--blue);margin-bottom:14px}
.foot-col a{display:block;font-size:10.5px;color:#555;text-decoration:none;line-height:25.5px}
.bottom-bar{position:absolute;top:3535px;left:0;width:1200px;height:72px;border-top:1px solid var(--line);text-align:center;font-size:10.5px;color:#666;padding-top:28px}
.bottom-bar .lang{position:absolute;right:28px;top:28px;color:#888}
</style>
</head>
<body>

<header class="site-header">
  <div class="brand"><span class="brand-mark"></span><span class="brand-name">dulvane</span></div>
  <nav class="main-nav">
    <a href="#">Home</a>
    <a href="#" class="active">Who We Are</a>
    <a href="#">What We Do</a>
    <a href="#">What Makes Us Different</a>
    <a href="#">Why It Matters</a>
    <a href="#" class="portal">CANDIDATE PORTAL</a>
    <a href="#">Contact Us</a>
    <a href="#">Blog</a>
  </nav>
</header>

<div class="dropdown">
  <a href="#">About Us</a>
  <a href="#">Mission</a>
  <a href="#">Vision and Purpose</a>
  <a href="#">Our Team</a>
</div>

<section class="hero" role="img" aria-label="Business team walking through a bright office corridor">
  <div class="hero-shade"></div>
  <h1 class="hero-title">We Are IT Recruiting &amp; IT Training Company</h1>
  <svg class="hero-arrow" style="left:64px" width="20" height="32" viewBox="0 0 20 32"><path d="M15 4 L5 16 L15 28" fill="none" stroke="#fff" stroke-width="4"/></svg>
  <svg class="hero-arrow" style="right:64px" width="20" height="32" viewBox="0 0 20 32"><path d="M5 4 L15 16 L5 28" fill="none" stroke="#fff" stroke-width="4"/></svg>
</section>

<h2 class="section-title" style="top:704px">WHAT WE DO</h2>
<div class="dots" style="top:751px"><span></span><span></span><span></span></div>

<div class="service" style="left:202px">
  <div class="service-head">
    <svg width="40" height="46" viewBox="0 0 40 46" fill="none" stroke="#1b5fa0" stroke-width="2"><circle cx="20" cy="14" r="9"/><path d="M4 44 C4 30 12 26 20 26 C28 26 36 30 36 44 Z"/><path d="M20 26 L17 34 L20 40 L23 34 Z"/></svg>
    <h3>IT Recruiting</h3>
  </div>
  <p>At vero eos et accusamus et iusto odio dignissimos ducimus qui blanditiis praesentium voluptatum deleniti atque corrupti quos dolores et quas molestias excepturi sint occaecati cupiditate</p>
  <a href="#" class="btn-sm">Read More</a>
</div>
<div class="service" style="left:474px">
  <div class="service-head">
    <svg width="44" height="46" viewBox="0 0 44 46" fill="none" stroke="#1b5fa0" stroke-width="2"><rect x="4" y="4" width="36" height="26"/><path d="M10 22 L18 14 L24 20 L34 10"/><path d="M14 30 L8 44 M30 30 L36 44 M22 30 L22 40"/></svg>
    <h3>IT Training</h3>
  </div>
  <p>At vero eos et accusamus et iusto odio dignissimos ducimus qui blanditiis praesentium voluptatum deleniti atque corrupti quos dolores et quas molestias excepturi sint occaecati cupiditate</p>
  <a href="#" class="btn-sm">Read More</a>
</div>
<div class="service" style="left:746px">
  <div class="service-head">
    <svg width="44" height="46" viewBox="0 0 44 46" fill="none" stroke="#1b5fa0" stroke-width="2"><rect x="8" y="10" width="28" height="20"/><path d="M2 36 L42 36 L38 30 L6 30 Z"/></svg>
    <h3>Hardware &amp; Software Sales</h3>
  </div>
  <p>At vero eos et accusamus et iusto odio dignissimos ducimus qui blanditiis praesentium voluptatum deleniti atque corrupti quos dolores et quas molestias excepturi sint occaecati cupiditate</p>
  <a href="#" class="btn-sm">Read More</a>
</div>

<section class="about">
  <h2 class="section-title" style="top:85px">ABOUT US</h2>
  <div class="dots" style="top:132px"><span></span><span></span><span></span></div>
  <p class="about-text">At vero eos et accusamus et iusto odio dignissimos ducimus qui blanditiis praesentium voluptatum deleniti atque corrupti quos dolores et quas molestias excepturi sint occaecati cupiditate non provident, similique sunt in culpa qui officia deserunt mollitia animi, id est laborum et dolorum fuga. Et harum quidem rerum facilis est et expedita distinctio. Nam libero tempore, cum soluta</p>
  <a href="#" class="btn-orange" style="left:529px;top:291px;width:142px;line-height:29px">LEARN MORE</a>
</section>

<h2 class="section-title" style="top:1582px">OUR TEAM</h2>
<div class="dots" style="top:1629px"><span></span><span></span><span></span></div>

<div class="member" style="left:202px;top:1696px">
  <div class="member-photo" role="img" aria-label="Portrait of the managing director"></div>
  <div class="member-role">Managing Director</div>
  <div class="member-name">Daniel Harper</div>
  <div class="member-org">Dulvane Business Solutions</div>
  <p class="member-bio">At vero eos et accusamus et iusto odio dignissimos ducimus qui blanditiis praesentium voluptatum deleniti atque corrupti quos dolores et quas molestias excepturi sint occaecati</p>
</div>
<div class="member" style="left:611px;top:1696px">
  <div class="member-photo" role="img" aria-label="Portrait of the managing partner" style="background:linear-gradient(160deg,#c9d3dc,#8d99a4)"></div>
  <div class="member-role">Managing Partner</div>
  <div class="member-name">Marcus Reed</div>
  <div class="member-org">Dulvane Business Solutions</div>
  <p class="member-bio">At vero eos et accusamus et iusto odio dignissimos ducimus qui blanditiis praesentium voluptatum deleniti atque corrupti quos dolores et quas molestias excepturi sint occaecati</p>
</div>
<div class="member" style="left:202px;top:1972px">
  <div class="member-photo" role="img" aria-label="Portrait of the team executive" style="background:linear-gradient(160deg,#e4e4e4,#a9a9ae)"></div>
  <div class="member-role">Team Excecutive</div>
  <div class="member-name">Kenji</div>
  <div class="member-org">Dulvane Business Solutions</div>
  <p class="member-bio">At vero eos et accusamus et iusto odio dignissimos ducimus qui blanditiis praesentium voluptatum deleniti atque corrupti quos dolores et quas molestias excepturi sint occaecati</p>
</div>
<div class="member" style="left:611px;top:1972px">
  <div class="member-photo" role="img" aria-label="Portrait of the manager" style="background:linear-gradient(160deg,#ececec,#bdb2a8)"></div>
  <div class="member-role">Manager</div>
  <div class="member-name">Laura Bennett</div>
  <div class="member-org">Dulvane Business Solutions</div>
  <p class="member-bio">At vero eos et accusamus et iusto odio dignissimos ducimus qui blanditiis praesentium voluptatum deleniti atque corrupti quos dolores et quas molestias excepturi sint occaecati</p>
</div>

<section class="contact">
  <h2 class="section-title" style="top:60px">CONTACT US</h2>
  <div class="dots" style="top:107px"><span></span><span></span><span></span></div>
  <div class="map" role="img" aria-label="Street map showing the office location"></div>
</section>

<h3 class="col-title" style="left:269px;top:2782px">CONTACT &nbsp;US</h3>
<h3 class="col-title" style="left:628px;top:2782px">ADDRESS</h3>

<div class="field" style="top:2835px">Name</div>
<div class="field" style="top:2891px">E-mail</div>
<div class="field" style="top:2947px">Phone</div>
<div class="field" style="top:3003px;height:88px">Message</div>
<a href="#" class="btn-orange" style="left:269px;top:3105px;width:92px;line-height:39px;font-size:15px;font-weight:400">SEND</a>

<div class="address">
  4120 Cedar Ridge<br>
  Way # 210 W. Larkford, Oregon<br>
  97990 ( Elmwood County )<br><br>
  E-MAIL : info@dulvanebiz.com<br><br>
  Phone : 555-014-2270
</div>

<footer class="site-footer">
  <div class="brand" style="top:64px"><span class="brand-mark"></span><span class="brand-name">dulvane</span></div>
  <a href="#" class="btn-orange" style="left:212px;top:117px;width:150px;line-height:29px">CANDIDATE PORTAL</a>
</footer>

<div class="foot-col" style="left:459px">
  <h4>Menu Links</h4>
  <a href="#">Home</a><a href="#">Who We Are</a><a href="#">What We Do</a><a href="#">What Makes Us Different</a><a href="#">Why It Matters</a><a href="#">Candidate Portal</a><a href="#">Contact Us</a><a href="#">Blog</a>
</div>
<div class="foot-col" style="left:666px">
  <h4>Who We Are ?</h4>
  <a href="#">IT Recruiting</a><a href="#">IT Training</a><a href="#">Hardware &amp; Software Sales</a><a href="#">Our Team</a>
</div>
<div class="foot-col" style="left:856px">
  <h4>What We Do ?</h4>
  <a href="#">About Us</a><a href="#">Mission</a><a href="#">Vision and Purpose</a><a href="#">Our Team</a>
</div>

<div class="bottom-bar">© 2016 Company Name &nbsp;|&nbsp; All Rights Reserved<span class="lang">CS</span></div>

</body>
</html>
```